KLT Motorhaus Automotive Repair and Service Shop

I need an informative and interactive website for my automotive service and repair shop. The website must give information about the shop, as well as the ability to make bookings and a forums page for our users to use and set up an account with us, in which we can give promotions via email. We are located in Pompano Beach Florida and our company name is KLT Motorhaus. Our color scheme is a red for accent and grey (neutral color) as a base. The design must communicate our message and be able to grow should we decide to retail parts in the future. One of the websites I take the highest inspiration from is http://www.brimfieldpanelworks.com/. Although I do not have as nearly as many certifications as them. Attached are some images of our shop so you can see how clean and modern our building is, and I would like our website to match our feel. Thank you.

Target Market(s)

Automotive Enthusiasts

Industry/Entity Type

Automotive

Contact Information for Business Card

KLT Motorhaus /954 718 4062 /dorian@kltmotorhaus.com/ 612 SW 27th Ave Pompano Beach FL 33069/ any other info needed please ask me

Coding

Coded - Design and coding required

Number of Pages Required

5+ page

Font styles to use
Sans Serif

Requirements
Must have
• Name, logo, contact info, location, phone number
Nice to have
• Building is very modern, would like a business card to match
Should not have
• Not to playful or vibrant

```html
<!DOCTYPE html>
<html lang="en">
<head>
<meta charset="utf-8">
<title>KLT Motorhaus — Automotive Service &amp; Repair</title>
<link rel="stylesheet" href="https://fonts.googleapis.com/css2?family=Syncopate:wght@400;700&family=Open+Sans:wght@400;700&display=swap">
<style>
:root{
  --red:#f0302d;
  --yellow:#e5c54f;
  --navy:#2e3562;
  --grey-light:#d4d4d4;
  --grey-mid:#c9c9c9;
  --grey-dark:#585858;
  --ink:#1e1e1e;
  --muted:#b9b9b9;
  --footer:#262626;
  --white:#ffffff;
}
*{box-sizing:border-box;margin:0;padding:0}
html,body{width:1200px;height:3599px;overflow:hidden;background:var(--white)}
body{font-family:'Syncopate',sans-serif;color:var(--ink);position:relative}
.abs{position:absolute}
.wide{font-family:'Syncopate',sans-serif;letter-spacing:.18em}
.btn{position:absolute;display:flex;align-items:center;justify-content:center;font-family:'Syncopate',sans-serif;font-size:9px;letter-spacing:.18em;color:var(--white);text-transform:uppercase}
.btn-yellow{background:var(--yellow)}
.btn-red{background:var(--red)}

/* top bar */
.topbar{left:0;top:0;width:1200px;height:91px;background:var(--grey-light)}
.brand{left:112px;top:22px;font-family:'Syncopate',sans-serif;font-weight:700;font-size:30px;color:var(--ink);letter-spacing:-.02em}
.toplinks{right:114px;top:43px;font-size:8px;letter-spacing:.12em;display:flex;gap:14px;color:var(--ink)}
.toplinks .call{color:var(--red)}

/* nav */
.nav{left:0;top:91px;width:1200px;height:75px;background:var(--white)}
.nav ul{list-style:none;position:absolute;left:115px;top:29px;display:flex;gap:0;font-size:10px;letter-spacing:.14em;color:#888}
.nav li{margin-right:32px}
.nav li.active{color:var(--red)}
.cart{left:972px;top:19px;width:114px;height:33px;border-radius:17px;background:var(--red);color:var(--white);font-family:'Open Sans',sans-serif;font-size:13px;display:flex;align-items:center;justify-content:center;gap:7px}

/* hero */
.hero{left:0;top:166px;width:1200px;height:451px;background:radial-gradient(ellipse at 50% 70%,#6d6a66 0%,#3b3835 55%,#1f1d1b 100%)}
.hero-title{left:0;width:1200px;text-align:center;color:var(--white)}
.hero-brand{top:30px;font-size:20px;letter-spacing:.22em}
.hero-tag{font-size:24px;letter-spacing:.3em;color:var(--yellow)}

/* welcome */
.section-title{left:0;width:1200px;text-align:center;font-size:25px;font-weight:700;letter-spacing:.3em;color:var(--ink)}
.form-panel{left:112px;top:707px;width:307px;height:374px;background:var(--navy)}
.form-panel h3{position:absolute;left:26px;top:28px;font-family:'Open Sans',sans-serif;font-weight:700;font-size:20px;color:var(--white)}
.field{position:absolute;background:var(--white);font-family:'Open Sans',sans-serif;font-size:12px;color:#9a9a9a;padding:0 10px;display:flex;align-items:center}
.acc-bar{left:446px;width:310px;height:41px;background:var(--grey-mid);color:var(--white);font-size:10px;letter-spacing:.18em;display:flex;align-items:center;padding-left:20px;gap:16px}
.acc-body{left:446px;top:754px;width:310px;height:280px;background:var(--grey-mid);color:var(--white);padding:20px 22px 0 22px;font-size:9.5px;line-height:15.9px;letter-spacing:.14em}
.free-panel{left:780px;top:707px;width:307px;height:374px;background:linear-gradient(135deg,#7a7a7a 0%,#3b3b3b 45%,#1c1c1c 100%)}
.free-text{left:780px;width:307px;text-align:center;font-size:32px;font-weight:700;letter-spacing:.25em;color:var(--yellow)}

/* offer */
.offer{left:0;top:1127px;width:1200px;height:597px;background:var(--grey-light)}
.card{position:absolute;top:1245px;width:307px;height:419px;background:var(--white)}
.card-img{position:absolute;left:0;top:0;width:307px;height:204px}
.card h4{position:absolute;left:0;top:224px;width:100%;text-align:center;font-weight:400;font-size:15px;letter-spacing:.2em}
.card p{position:absolute;left:30px;top:256px;width:247px;text-align:center;font-size:7px;line-height:16px;letter-spacing:.14em;color:var(--muted)}

/* why */
.why-head{font-size:17px;letter-spacing:.24em;line-height:33px;color:var(--ink)}
.why-text{width:255px;font-size:7px;line-height:15.8px;letter-spacing:.14em;color:var(--muted)}
.right{text-align:right}

/* split */
.split-head{font-size:32px;font-weight:700;letter-spacing:.3em;line-height:54px}
.split-text{width:390px;font-size:7.5px;line-height:15.8px;letter-spacing:.12em}

/* commercial */
.commercial{left:0;top:2703px;width:1200px;height:583px;background:radial-gradient(ellipse at 50% 50%,#4a4542 0%,#2b2725 60%,#161413 100%)}

/* footer */
.footer{left:0;top:3286px;width:1200px;height:313px;background:var(--footer);color:var(--white)}
.foot-h{font-family:'Open Sans',sans-serif;font-weight:700;font-size:15px;color:var(--white)}
.foot-small{font-size:7.5px;line-height:15.6px;letter-spacing:.12em;color:var(--white)}
.foot-links{list-style:none;font-size:9px;letter-spacing:.16em}
.foot-links li{height:27.5px}
.foot-links li::before{content:"› ";color:#888}
.contact-line{font-size:9.5px;letter-spacing:.16em;color:var(--red);line-height:15px}
.social{display:flex;gap:12px}
.social span{width:7px;height:7px;border-radius:50%;background:var(--white);display:block}
</style>
</head>
<body>

<!-- top bar -->
<header class="abs topbar">
  <div class="abs brand">KLT MOTORHAUS</div>
  <div class="abs toplinks">
    <span class="call">Call us now: 954 718 4062</span><span>|</span>
    <span>Find us on map</span><span>|</span>
    <span>Sitemap</span><span>|</span>
    <span>English</span>
  </div>
</header>

<nav class="abs nav">
  <ul>
    <li class="active">Home</li>
    <li>Services</li>
    <li>About us</li>
    <li>Forum</li>
    <li>Shop</li>
    <li>Contact</li>
  </ul>
  <div class="abs cart">
    <svg width="18" height="15" viewBox="0 0 18 15" fill="none" stroke="#fff" stroke-width="1.5"><path d="M1 1h3l2 9h9l2-7H5"/><circle cx="7.5" cy="13" r="1.3" fill="#fff"/><circle cx="14" cy="13" r="1.3" fill="#fff"/></svg>
    <span>0 ITEMS</span>
  </div>
</nav>

<!-- hero -->
<section class="abs hero" role="img" aria-label="Workshop background with three tuned sports cars in grey, green and red"></section>
<div class="abs hero-title hero-brand" style="top:196px">KLT Motorhaus</div>
<div class="abs hero-title hero-tag" style="top:244px">Fine tuning your</div>
<div class="abs hero-title hero-tag" style="top:286px">automotive service</div>
<div class="btn btn-yellow" style="left:440px;top:342px;width:116px;height:41px">Get quote</div>
<div class="btn btn-red" style="left:581px;top:342px;width:173px;height:41px">Account with us</div>

<!-- welcome -->
<h2 class="abs section-title" style="top:650px">Welcome</h2>

<form class="abs form-panel">
  <h3>Request Information</h3>
  <div class="field" style="left:26px;top:73px;width:255px;height:36px">Enter Name</div>
  <div class="field" style="left:26px;top:127px;width:115px;height:36px">Email</div>
  <div class="field" style="left:167px;top:127px;width:114px;height:36px">Phone</div>
  <div class="field" style="left:26px;top:182px;width:115px;height:36px;color:#333;justify-content:space-between">-Vehicle Mode<span style="font-size:8px">▼</span></div>
  <div class="field" style="left:167px;top:182px;width:114px;height:36px">Reservation Date</div>
  <div class="field" style="left:26px;top:237px;width:255px;height:62px;align-items:flex-start;padding-top:8px;line-height:16px">Your cover letter/message sent to the employer</div>
  <div class="btn btn-yellow" style="left:26px;top:317px;width:115px;height:35px">Submit</div>
</form>

<div class="abs acc-bar" style="top:707px"><span style="font-size:16px">—</span>Who we are?</div>
<div class="abs acc-body">
  Lorem Ipsum is simply dummy text of the printing and typesetting industry. Lorem Ipsum has been the industry's standard dummy text ever since the 1500s, when an unknown printer took a galley of type and scrambled it to make a type specimen book. It has survived not only five centuries, but also the leap into electronic typesetting, remaining essentially unchanged.
  <div style="margin-top:10px;display:flex;gap:16px;align-items:center"><span style="font-size:18px">+</span>Car body repairing</div>
</div>
<div class="abs acc-bar" style="top:1039px"><span style="font-size:18px">+</span>24/7 Serivces</div>

<div class="abs free-panel" role="img" aria-label="Mechanic working on an engine with gloved hands"></div>
<div class="abs free-text" style="top:808px">FREE</div>
<div class="abs free-text" style="top:860px">CHECK</div>
<div class="btn btn-red" style="left:837px;top:964px;width:193px;height:52px">Book appointment</div>

<!-- what we offer -->
<section class="abs offer"></section>
<h2 class="abs section-title" style="top:1170px">What we offer</h2>

<article class="card" style="left:112px">
  <div class="card-img" role="img" aria-label="Engine block on a workshop stand" style="background:linear-gradient(135deg,#6f86a6,#3c4450 60%,#22262c)"></div>
  <h4>Multiple Options</h4>
  <p>Lorem Ipsum is simply dummy text of the printing and typesetting industry. Lorem Ipsum has been the industry's standard dummy text ever since the 1500s</p>
  <div class="btn btn-yellow" style="left:96px;top:353px;width:115px;height:34px">More</div>
</article>
<article class="card" style="left:446px">
  <div class="card-img" role="img" aria-label="Mechanic installing a part under the hood" style="background:linear-gradient(135deg,#a9abae,#55585c 55%,#2a2c2f)"></div>
  <h4>Deliver &amp; Install</h4>
  <p>Lorem Ipsum is simply dummy text of the printing and typesetting industry. Lorem Ipsum has been the industry's standard dummy text ever since the 1500s</p>
  <div class="btn btn-yellow" style="left:96px;top:353px;width:115px;height:34px">More</div>
</article>
<article class="card" style="left:777px">
  <div class="card-img" role="img" aria-label="White SUV on a lift in a service bay" style="background:linear-gradient(135deg,#8a9bb0,#c6cbd1 50%,#5a6572)"></div>
  <h4>Service &amp; Repairs</h4>
  <p>Lorem Ipsum is simply dummy text of the printing and typesetting industry. Lorem Ipsum has been the industry's standard dummy text ever since the 1500s</p>
  <div class="btn btn-yellow" style="left:96px;top:353px;width:115px;height:34px">More</div>
</article>

<!-- why choose us -->
<h2 class="abs section-title" style="top:1770px">Why choose us</h2>
<div class="abs" role="img" aria-label="Mechanic in gloves fitting a wheel" style="left:425px;top:1841px;width:360px;height:398px;background:linear-gradient(135deg,#d9d9d9,#8d8d8d 55%,#4a4a4a);box-shadow:0 6px 16px rgba(0,0,0,.25)"></div>

<div class="abs why-head" style="left:106px;top:1836px">Fast Low<br>Cost Freight</div>
<p class="abs why-text" style="left:112px;top:1913px">Lorem ipsum dolor sit amet, consectetur adipiscing elit, sed do eiusmod tempor incididunt ut labore et dolore magna aliqua. Quis ipsum suspendisse ultrices gravida. Risus commodo viverra maecenas accumsan lacus vel facilisis.</p>
<div class="abs why-head" style="left:106px;top:2058px">Automotive service<br>and repair shop</div>
<p class="abs why-text" style="left:112px;top:2134px">Lorem ipsum dolor sit amet, consectetur adipiscing elit, sed do eiusmod tempor incididunt ut labore et dolore magna aliqua. Quis ipsum suspendisse ultrices gravida. Risus commodo viverra maecenas accumsan lacus vel facilisis.</p>

<div class="abs why-head right" style="right:113px;top:1836px">Customer<br>Service</div>
<p class="abs why-text right" style="right:113px;top:1913px">Lorem ipsum dolor sit amet, consectetur adipiscing elit, sed do eiusmod tempor incididunt ut labore et dolore magna aliqua. Quis ipsum suspendisse ultrices gravida. Risus commodo viverra maecenas accumsan lacus vel facilisis.</p>
<div class="abs why-head right" style="right:113px;top:2058px">A Decade<br>in Business</div>
<p class="abs why-text right" style="right:113px;top:2134px">Lorem ipsum dolor sit amet, consectetur adipiscing elit, sed do eiusmod tempor incididunt ut labore et dolore magna aliqua. Quis ipsum suspendisse ultrices gravida. Risus commodo viverra maecenas accumsan lacus vel facilisis.</p>

<!-- split band -->
<svg class="abs" style="left:0;top:2305px" width="1200" height="398" viewBox="0 0 1200 398">
  <rect width="1200" height="398" fill="#585858"/>
  <polygon points="668,0 1200,0 1200,398 601,398" fill="#f0302d"/>
</svg>
<div class="abs split-head" style="left:112px;top:2350px;color:var(--white)">Find the<br>Right services</div>
<p class="abs split-text" style="left:112px;top:2476px;color:var(--white)">Lorem ipsum dolor sit amet, consectetur adipiscing elit, sed do eiusmod tempor incididunt ut labore et dolore magna aliqua. Quis ipsum suspendisse ultrices gravida. Risus commodo viverra maecenas accumsan lacus vel facilisis.</p>
<div class="btn btn-red" style="left:112px;top:2582px;width:193px;height:50px">Shop now</div>

<div class="abs split-head right" style="right:113px;top:2350px;color:#2a2a2a">Top<br>Brands</div>
<p class="abs split-text right" style="right:113px;top:2476px;color:var(--white)">Lorem ipsum dolor sit amet, consectetur adipiscing elit, sed do eiusmod tempor incididunt ut labore et dolore magna aliqua. Quis ipsum suspendisse ultrices gravida. Risus commodo viverra maecenas accumsan lacus vel facilisis.</p>
<div class="btn btn-yellow" style="left:894px;top:2582px;width:193px;height:50px">Forum page</div>

<!-- commercial -->
<section class="abs commercial" role="img" aria-label="Mechanic's hands working in an engine bay"></section>
<div class="abs hero-title" style="top:2760px;font-size:26px;font-weight:700;letter-spacing:.3em">Watch</div>
<div class="abs hero-title" style="top:2812px;font-size:26px;font-weight:700;letter-spacing:.3em">Our commercial</div>

<svg class="abs" style="left:306px;top:2892px" width="588" height="344" viewBox="0 0 588 344">
  <rect width="588" height="302" fill="#d11b1b"/>
  <circle cx="295" cy="148" r="67" fill="#fff"/>
  <polygon points="275,115 275,181 330,148" fill="#e01f1f"/>
  <rect y="302" width="588" height="42" fill="#1c1915"/>
  <rect y="302" width="588" height="5" fill="#6b6b6b"/>
  <rect y="302" width="185" height="5" fill="#d11b1b"/>
  <circle cx="185" cy="304" r="4" fill="#fff"/>
  <polygon points="18,315 18,333 32,324" fill="#fff"/>
  <polygon points="50,317 50,331 59,324" fill="#fff"/><polygon points="59,317 59,331 68,324" fill="#fff"/><rect x="68" y="317" width="2.5" height="14" fill="#fff"/>
  <polygon points="92,320 98,320 104,315 104,333 98,328 92,328" fill="#fff"/>
  <rect x="116" y="323" width="38" height="2.5" fill="#fff"/><circle cx="150" cy="324" r="3.5" fill="#fff"/>
  <text x="417" y="328" font-family="Open Sans,sans-serif" font-size="11" fill="#fff">2:15 / 6:55</text>
  <circle cx="490" cy="324" r="6" fill="none" stroke="#fff" stroke-width="3"/>
  <rect x="514" y="317" width="20" height="14" fill="none" stroke="#fff" stroke-width="2"/>
  <path d="M550 321v-5h5M565 316h5v5M570 328v5h-5M555 333h-5v-5" fill="none" stroke="#fff" stroke-width="2"/>
</svg>

<!-- footer -->
<footer class="abs footer"></footer>
<div class="abs" style="left:168px;top:3343px;font-family:'Syncopate',sans-serif;font-weight:700;font-size:19px;color:var(--white)">KLT MOTORHAUS</div>
<p class="abs foot-small" style="left:168px;top:3389px;width:182px">Lorem ipsum dolor sit amet, consectetur adipiscing elit, sed do eiusmod tempor ut labore et dolore magna aliqua. Quis ipsum suspendisse ultrices gravida. Risus commodo viverra maecenas accumsan lacus vel facilisis.</p>

<div class="abs foot-h" style="left:398px;top:3346px">Links</div>
<ul class="abs foot-links" style="left:398px;top:3393px;color:var(--white)">
  <li>Home</li><li>Services</li><li>About us</li><li>Forum</li><li>Shop</li><li>Contact</li>
</ul>

<div class="abs foot-h" style="left:620px;top:3346px">Contact Us</div>
<svg class="abs" style="left:590px;top:3393px" width="20" height="20" viewBox="0 0 20 20"><path d="M4 2l4 1 1 4-2 2c1 2 3 4 5 5l2-2 4 1 1 4-2 2C9 19 1 11 2 4z" fill="#f0302d"/></svg>
<div class="abs contact-line" style="left:623px;top:3395px">954 718 4062</div>
<svg class="abs" style="left:589px;top:3445px" width="20" height="28" viewBox="0 0 20 28"><path d="M10 1C5 1 1 5 1 10c0 7 9 17 9 17s9-10 9-17c0-5-4-9-9-9z" fill="#f0302d"/><circle cx="10" cy="10" r="3.5" fill="#262626"/></svg>
<div class="abs contact-line" style="left:623px;top:3448px">612 SW 27th Ave<br>Pompano Beach FL<br>33069</div>
<svg class="abs" style="left:588px;top:3522px" width="26" height="18" viewBox="0 0 26 18"><rect x="1" y="1" width="24" height="16" fill="none" stroke="#f0302d" stroke-width="2"/><path d="M1 1l12 9 12-9" fill="none" stroke="#f0302d" stroke-width="2"/></svg>
<div class="abs contact-line" style="left:623px;top:3523px">dorian@kltmotorhaus.com</div>

<div class="abs foot-h" style="left:844px;top:3346px">Get Our Newsletter</div>
<div class="abs" style="left:844px;top:3395px;width:187px;height:32px;border-radius:16px;background:#5a5a5a;display:flex;align-items:center;justify-content:space-between;padding:0 18px;font-family:'Open Sans',sans-serif;font-size:12px;color:#bdbdbd"><span>EMAIL</span><span style="color:#fff">›</span></div>
<div class="abs" style="left:844px;top:3438px;width:200px;font-family:'Open Sans',sans-serif;font-size:11.5px;line-height:19px;color:#d8d8d8"><span style="display:inline-block;width:9px;height:9px;background:#fff;margin-right:4px"></span>I agree that my submitted data is being collected and stored.</div>
<div class="abs social" style="left:888px;top:3528px"><span></span><span></span><span></span><span></span><span></span><span></span><span></span><span></span></div>

<div class="abs" style="left:168px;top:3576px;font-size:6.5px;letter-spacing:.14em;color:var(--white)">KLT Motorhaus© 2020. All rights reserved.</div>

</body>
</html>
```